Company producing high tech raw materials for the bakery industry needs new packaging design

We need a new design for the bag containing our products.

We are a producer of chemical and high tech raw materials for the bakery and confectionery sectors (we have small customers & also large industrial customers).

Our profile is in between food and pharmaceuticals. So the new design needs to present foremostly seriousness and reliability, but still not being blunt and boring as it contains exciting cutting edge food technology ingredients.

We have 3 different sizes of bags to contain our products, (which is in the form of powder like flour). 650x400x130 for 10 kgs, 700x460x130 for 15 kgs, 900x500x130 for 25 kgs, so the design should look good in all three sizes. Bags are from thick paper.

I am attaching pictures of our current (very badly designed blue-grey) bag and some pictures of competition bags, so that you get an idea of how the bags in the industry generally are.

The new bag should contain the logo (attached). The colors used in the logo are CMYK , DARK BLUE 100,83,5,27 LIGHT BLUE 60,40,0,0. Our primary colors are like the ones in the logo and as secondary we have grey and yellow (orange). Maximum number of different colors that can be used in the new design is 4 (because the printing cost is much more expensive with more than that).

FYI on the bag, as you can see in the attached pictures of our current bag, must be an A5 - A4 size label and the top opening is sewed.

Please do not hesitate to contact us for any further questions or clarification.

Requirements
Must have
• Take into account the label and the closing on top of the bag
3 bag sizes
Highly visible logo

```html
<!DOCTYPE html>
<html lang="en">
<head>
<meta charset="utf-8">
<title>Velkorn bakery ingredients bag</title>
<link href="https://fonts.googleapis.com/css2?family=Questrial&display=swap" rel="stylesheet">
<style>
  :root {
    --page: #ecedf0;
    --bag: #ffffff;
    --blue-dark: #213a74;
    --blue-light: #6e8bc7;
  }
  * { margin: 0; padding: 0; box-sizing: border-box; }
  html, body {
    width: 1200px;
    height: 894px;
    overflow: hidden;
    background: var(--page);
  }
  .bag-face {
    position: absolute;
    left: 317px;
    top: 17px;
    width: 566px;
    height: 860px;
    background: var(--bag);
    overflow: hidden;
  }
  .brand-tab {
    position: absolute;
    left: 136px;
    top: 0;
    width: 295px;
    height: 322px;
    background: var(--blue-dark);
    border-radius: 0 0 78px 78px;
    display: flex;
    flex-direction: column;
    align-items: center;
    justify-content: flex-end;
    padding-bottom: 56px;
  }
  .brand-row {
    display: flex;
    align-items: center;
    gap: 12px;
  }
  .brand-dot {
    width: 18px;
    height: 18px;
    border-radius: 50%;
    background: var(--blue-light);
  }
  .brand-name {
    font-family: "Questrial", sans-serif;
    font-size: 52px;
    line-height: 1;
    color: #ffffff;
    letter-spacing: 0.5px;
  }
  .brand-sub {
    margin-top: 6px;
    font-family: "Questrial", sans-serif;
    font-size: 16px;
    letter-spacing: 1.6px;
    color: var(--blue-light);
  }
  .hero-graphic {
    position: absolute;
    left: 138px;
    top: 588px;
    width: 428px;
    height: 272px;
  }
</style>
</head>
<body>
  <main class="bag-face">
    <div class="brand-tab">
      <div class="brand-row">
        <span class="brand-dot"></span>
        <span class="brand-name">Velkorn</span>
      </div>
      <p class="brand-sub">ΑΦΟΙ ΚΑΡΑΛΙΔΗ</p>
    </div>
    <svg class="hero-graphic" viewBox="0 0 428 272" role="img" aria-label="Large decorative brand graphic in dark and light blue at the bottom of the bag">
      <defs>
        <linearGradient id="heroTone" x1="0" y1="1" x2="1" y2="0">
          <stop offset="0" stop-color="#213a74"/>
          <stop offset="1" stop-color="#6e8bc7"/>
        </linearGradient>
      </defs>
      <path d="M0 272 C10 150 160 40 428 20 L428 272 Z" fill="url(#heroTone)"/>
    </svg>
  </main>
</body>
</html>
```